Homepage Mockup for Chiropractor

We need a full-width layout

Redesigning this website: [login to view URL]

Homepage mockup only (psd)

Colors: Blues, natural tones

Please make sections less cluttered and more organized

Needs contact info and social in header

```html
<!DOCTYPE html>
<html lang="en">
<head>
<meta charset="utf-8">
<title>Ridgeview Spine & Injury Clinic — Home</title>
<link href="https://fonts.googleapis.com/css2?family=Open+Sans:wght@400;600;700;800&family=Tinos:wght@400;700&family=Roboto:wght@400;500&display=swap" rel="stylesheet">
<style>
:root{
  --blue:#1b5eab;
  --blue-dark:#154f92;
  --navy:#1c3557;
  --hero-a:#d4d4d4;
  --hero-b:#a9a9a9;
  --text:#555;
  --heading:#2b2b2b;
  --light:#f3f3f3;
  --field:#ececec;
  --footer:#232323;
  --red:#d9322e;
  --white:#fff;
}
*{box-sizing:border-box;margin:0;padding:0}
html,body{width:1200px;height:4039px;overflow:hidden}
body{position:relative;font-family:"Open Sans",Arial,sans-serif;color:var(--text);background:var(--white)}
.abs{position:absolute}

.site-header{left:0;top:0;width:1200px;height:138px;background:linear-gradient(180deg,#555,#3f3f3f)}
.brand{left:70px;top:0;width:330px;height:138px;background:var(--white);border-radius:0 0 60px 60px;display:flex;align-items:center;justify-content:center;gap:12px}
.brand-dot{width:38px;height:38px;border-radius:50%;background:#3d3d3d}
.brand-name{font-family:"Open Sans",sans-serif;font-weight:700;font-size:21px;color:#3d3d3d;line-height:1.15}
.header-contact{right:99px;top:6px;text-align:right;color:var(--white);font-family:"Tinos",serif}
.header-contact .addr{font-size:17px;color:#e6e6e6}
.header-contact .phone{font-size:28px;line-height:34px}
.header-contact .visit{font-size:21px;line-height:26px}

.main-nav{left:0;top:138px;width:1200px;height:39px;background:var(--blue)}
.main-nav .active-bg{left:99px;top:0;width:88px;height:39px;background:#5a5a5a}
.main-nav a{position:absolute;top:0;line-height:39px;transform:translateX(-50%);color:var(--white);font-size:13px;font-weight:600;text-decoration:none;white-space:nowrap}

.hero{left:0;top:177px;width:1200px;height:529px;background:linear-gradient(135deg,var(--hero-a),#bdbdbd 50%,var(--hero-b));overflow:hidden}
.hero-photo{left:604px;top:0;width:596px;height:529px;background:linear-gradient(180deg,#cfcfcf,#e8e2dc 40%,#f5f3f1)}
.hero h1{left:129px;top:210px;font-size:34px;line-height:41px;font-weight:800;color:var(--navy);letter-spacing:.3px}
.hero-wave{left:0;top:420px}

.about-shadow{left:88px;top:781px;width:348px;height:396px;background:var(--blue)}
.about-photo{left:97px;top:769px;width:350px;height:400px;background:linear-gradient(180deg,#9a9a9a,#3b3b3b 70%,#222)}
.about-text{left:488px;top:768px;width:615px}
.about-text h2{font-size:20px;font-weight:700;color:var(--heading);margin-bottom:14px}
.about-text p{font-size:15px;line-height:23.5px;color:var(--text);margin-bottom:23px}
.btn-solid{display:inline-block;background:var(--blue);color:var(--white);font-size:13px;font-weight:700;padding:4px 13px}

.promise{left:0;top:1244px;width:1200px;height:274px;background:var(--blue)}
.promise-area{left:0;top:1518px;width:1200px;height:317px;background:var(--light)}
.promise h2{left:0;top:52px;width:1200px;text-align:center;color:var(--white);font-size:23px;line-height:29px;font-weight:700}
.video{left:264px;top:1407px;width:671px;height:384px;background:var(--white);padding:9px;box-shadow:0 2px 6px rgba(0,0,0,.2)}
.video-screen{width:100%;height:100%;background:linear-gradient(90deg,#111,#3a3a3a 55%,#1a1a1a);display:flex;align-items:center;justify-content:center}

.service{top:1835px;width:235px}
.service-img{width:235px;height:146px}
.service h3{margin-top:36px;font-size:15px;font-weight:700;color:var(--heading)}
.service p{margin-top:10px;font-size:13px;line-height:17.5px;color:var(--text);height:70px}
.btn-outline{display:inline-block;margin-top:25px;border:2px solid var(--blue);color:var(--blue);font-size:12px;font-weight:700;padding:1px 10px}
.btn-outline.filled{background:var(--blue);color:var(--white)}

.patients{left:0;top:2215px;width:1200px;height:452px;background:linear-gradient(180deg,var(--blue),var(--blue-dark))}
.patients h2{left:0;top:42px;width:1200px;text-align:center;font-size:22px;font-weight:700;color:var(--white)}
.patients p{left:320px;top:77px;width:560px;text-align:center;font-size:15px;line-height:18px;color:#e3ecf7}
.form-card{left:311px;top:2353px;width:578px;height:348px;background:var(--white);box-shadow:0 8px 18px rgba(0,0,0,.15)}
.form-card label{position:absolute;font-family:"Roboto",sans-serif;font-size:10px;font-weight:500;color:#333}
.form-card label span{color:#999;font-weight:400}
.form-card .field{position:absolute;background:var(--field)}
.submit{left:252px;top:284px;width:75px;height:28px;background:var(--blue);color:var(--white);font-size:10px;font-weight:700;text-align:center;line-height:28px}

.testimonial h2{left:0;top:2764px;width:1200px;text-align:center;font-family:"Roboto",sans-serif;font-weight:500;font-size:21px;color:#333}
.avatar{left:558px;top:2828px;width:76px;height:76px;background:linear-gradient(180deg,#e4e8ec,#c8d3dc)}
.quote{left:170px;top:2923px;width:860px;padding:0 44px;text-align:center;font-size:16px;line-height:22px;color:#444}
.quote-mark{font-family:"Tinos",serif;font-weight:700;font-size:40px;color:#333;position:absolute;line-height:1}
.client{left:0;top:2978px;width:1200px;text-align:center;font-size:15px;color:#333}
.arrows{left:568px;top:3009px;display:flex;gap:3px}
.arrows span{width:27px;height:27px;background:#cfcfcf;display:flex;align-items:center;justify-content:center}

.blog{left:0;top:3093px;width:1200px;height:519px;background:var(--light)}
.blog h2{left:0;top:47px;width:1200px;text-align:center;font-family:"Roboto",sans-serif;font-weight:500;font-size:22px;color:#333}
.blog .lead{left:160px;top:94px;width:880px;text-align:center;font-size:14px;line-height:18px;color:var(--text)}
.post{top:3256px;width:317px;height:295px;background:var(--white)}
.post-img{width:317px;height:167px}
.post-date{left:11px;top:148px;width:47px;height:43px;background:var(--blue);color:var(--white);text-align:center;font-size:14px;font-weight:700;line-height:17px;padding-top:5px}
.post h3{left:73px;top:186px;font-size:13px;font-weight:700;color:#222}
.post .by{left:73px;top:205px;font-size:10px;color:#444}
.post p{left:13px;top:240px;width:295px;font-size:13px;line-height:18px;color:var(--text)}
.post p em{font-style:normal;color:var(--red)}

.site-footer{left:0;top:3612px;width:1200px;height:427px;background:var(--footer);color:var(--white)}
.site-footer h4{position:absolute;top:46px;font-family:"Roboto",sans-serif;font-weight:400;font-size:21px}
.foot-about{left:97px;top:106px;width:280px;font-size:13px;line-height:16px}
.foot-line{position:absolute;left:97px;font-size:13px;line-height:16px;display:flex;gap:12px}
.links{position:absolute;top:96px;font-size:13px;line-height:30.5px}
.links div::before{content:"";display:inline-block;border-left:5px solid #2e8be0;border-top:4px solid transparent;border-bottom:4px solid transparent;margin-right:12px}
.hours{left:784px;top:96px;width:318px;font-size:13px}
.hours div{display:flex;justify-content:space-between;height:51px;padding-top:13px;border-bottom:1px solid #3a3a3a}
.foot-bottom{left:97px;top:382px;font-size:13px}
.foot-bottom a{color:#2e8be0;text-decoration:none}
.social{top:380px;width:31px;height:31px;background:#1b78d4}
</style>
</head>
<body>

<header class="abs site-header">
  <div class="abs brand"><span class="brand-dot"></span><span class="brand-name">Birchline Spine<br>&amp; Wellness</span></div>
  <div class="abs header-contact">
    <div class="addr">1820 Canyon Ridge Rd., Ridgeview, Texas 70142</div>
    <div class="phone">(555) 014-2290</div>
    <div class="visit">Be sure to visit our Birchline page at</div>
    <div class="visit">www.BirchlineCare.example</div>
  </div>
</header>

<nav class="abs main-nav">
  <div class="abs active-bg"></div>
  <a style="left:143px">HOME</a>
  <a style="left:251px">ABOUT US</a>
  <a style="left:389px">CHIROPRACTIC</a>
  <a style="left:519px">PATIENT</a>
  <a style="left:627px">STORIES</a>
  <a style="left:747px">CAR WRECK</a>
  <a style="left:857px">BLOG</a>
  <a style="left:949px">NEWS</a>
  <a style="left:1054px">CONTACT</a>
</nav>

<section class="abs hero">
  <div class="abs hero-photo" role="img" aria-label="Smiling family of four in white clothes"></div>
  <h1 class="abs">WE'RE HERE FOR YOUR<br>WHOLE FAMILY</h1>
  <svg class="abs hero-wave" width="1200" height="110" viewBox="0 0 1200 110">
    <path d="M0 110 L0 90 C160 20 330 5 520 40 C720 78 900 70 1060 20 C1120 2 1170 -2 1200 0 L1200 110 Z" fill="#fff"/>
    <path d="M0 90 C160 20 330 5 520 40 C720 78 900 70 1060 20 C1120 2 1170 -2 1200 0" fill="none" stroke="#1b5eab" stroke-width="4"/>
  </svg>
</section>

<section class="about">
  <div class="abs about-shadow"></div>
  <div class="abs about-photo" role="img" aria-label="Portrait of Dr. Alan Mercer"></div>
  <div class="abs about-text">
    <h2>ABOUT DR. ALAN MERCER</h2>
    <p>Let me introduce myself to you!</p>
    <p>I am a Panhandle area native. I was born right here in Ridgeview and raised in Millbrook, TX just North of Ridgeview.</p>
    <p>I was an athlete in high school and college which is what led me to discover chiropractic. I was a freshman in high school and was skiing in the mountains. I hit a jump just a little bit wrong and came down on top of my head. I was in severe pain for months. We had appointments with medical doctors, osteopaths, etc. My mother finally talked me into trying a chiropractor. I made my appointment and thank God that I did. The chiropractor had me out of pain in three weeks and I had suffered for six months! You could say that I was going to a chiro any time I hurt from then on.</p>
    <span class="btn-solid">READ MORE</span>
  </div>
</section>

<section class="abs promise">
  <h2 class="abs">SE HABLA ESPANOL, NO CONTRACTS, USUALLY SAME DAY<br>APPOINTMENTS, NO CHARGE CONSULTATIONS....</h2>
</section>
<div class="abs promise-area"></div>
<div class="abs video">
  <div class="video-screen" role="img" aria-label="Introductory video of the doctor">
    <svg width="46" height="46" viewBox="0 0 46 46"><rect width="46" height="46" rx="8" fill="rgba(0,0,0,.55)"/><path d="M17 13 L33 23 L17 33 Z" fill="#fff"/></svg>
  </div>
</div>

<section class="services">
  <div class="abs service" style="left:97px">
    <div class="service-img" role="img" aria-label="Patient on a decompression table" style="background:linear-gradient(180deg,#e8e6e2,#8a8f9a 60%,#2e4f8f)"></div>
    <h3>SPINAL DECOMPRESSION</h3>
    <p>Spinal Decompression Therapy is a non-surgical therapy to relieve back pain and other problems associated with spinal disc</p>
    <span class="btn-outline">LEARN MORE</span>
  </div>
  <div class="abs service" style="left:353px">
    <div class="service-img" role="img" aria-label="Cold laser treatment on a shoulder" style="background:linear-gradient(180deg,#f2f2f2,#d9b79d 60%,#c99a7c)"></div>
    <h3>COLD LASER</h3>
    <p>Ridgeview Cold Laser Therapy is a relatively new process that has emerged. Cold Laser Therapy, also known as Low Level</p>
    <span class="btn-outline filled">LEARN MORE</span>
  </div>
  <div class="abs service" style="left:605px">
    <div class="service-img" role="img" aria-label="Therapist giving a neck massage" style="background:linear-gradient(180deg,#eef1f4,#d8dde2 60%,#b9c3cc)"></div>
    <h3>MASSAGE THERAPY</h3>
    <p>Ridgeview Spine &amp; Injury Chiropractic Center has the best Ridgeview massage therapy for all of your aches and pains.</p>
    <span class="btn-outline">LEARN MORE</span>
  </div>
  <div class="abs service" style="left:864px">
    <div class="service-img" role="img" aria-label="3D view of the human skeleton" style="background:radial-gradient(circle at 50% 45%,#3e6fa8,#0d2444 75%)"></div>
    <h3>3D BODY VIEW</h3>
    <p>3D SpineScope is the first true color 3D imaging device to be released in the chiropractic profession. It is adding a new dimension</p>
    <span class="btn-outline">LEARN MORE</span>
  </div>
</section>

<section class="abs patients">
  <h2 class="abs">NEW PATIENTS</h2>
  <p class="abs">Lorem ipsum dolor sit amet, consectetur adipiscing elit. Vestibulum vulputate nunc non porttitor quis dignissim mauris pretium in.</p>
</section>
<form class="abs form-card">
  <label style="left:37px;top:40px">YOUR NAME*</label>
  <label style="left:301px;top:40px">YOUR PHONE*</label>
  <div class="field" style="left:37px;top:58px;width:242px;height:28px"></div>
  <div class="field" style="left:301px;top:58px;width:241px;height:28px"></div>
  <label style="left:37px;top:112px">I'D LIKE TO DISCUSS ABOUT*</label>
  <div class="field" style="left:37px;top:130px;width:505px;height:28px"></div>
  <label style="left:37px;top:183px">ADDITIONAL NOTE <span>(OPTIONAL)</span></label>
  <div class="field" style="left:37px;top:201px;width:505px;height:59px"></div>
  <div class="abs submit">SUBMIT</div>
</form>

<section class="testimonial">
  <h2 class="abs">LOVELY CLIENT COMMENT</h2>
  <div class="abs avatar" role="img" aria-label="Client photo"></div>
  <div class="abs quote">
    <span class="quote-mark" style="left:12px;top:-6px">“</span>
    We are committed to providing you with the best, the most innovative, and the most modern and individually customized treatment available. We are your chiropractor in Ridgeview.
    <span class="quote-mark" style="right:12px;top:12px">”</span>
  </div>
  <div class="abs client">Dana Reyes, CEO</div>
  <div class="abs arrows">
    <span><svg width="8" height="10"><path d="M6 1 L2 5 L6 9" stroke="#fff" stroke-width="1.5" fill="none"/></svg></span>
    <span><svg width="8" height="10"><path d="M2 1 L6 5 L2 9" stroke="#fff" stroke-width="1.5" fill="none"/></svg></span>
  </div>
</section>

<section class="abs blog">
  <h2 class="abs">LATEST BLOG</h2>
  <p class="abs lead">Lorem ipsum dolor sit amet, consectetur adipiscing elit. Proin id lectus faucibus, pretium felis ut, tincidunt metus. Mauris viverra, eros quis dapibus auctor, neque purus molestie dolor, nec iaculis massa nisl ut urna.</p>
</section>
<article class="abs post" style="left:91px">
  <div class="post-img" role="img" aria-label="Patient receiving a back massage" style="background:linear-gradient(90deg,#f1f1f1,#c9c9c9 60%,#2d5d9b)"></div>
  <div class="abs post-date">20<br>OCT</div>
  <h3 class="abs">LOREM IPSUM DOLOR SIT</h3>
  <div class="abs by">BY: ADMIN</div>
  <p class="abs">Lorem ipsum dolor sit amet, con sec tetur adipiscing elit. Duis commodo augue nec elit pellentesque molestie. <em>+ Read More..</em></p>
</article>
<article class="abs post" style="left:435px">
  <div class="post-img" role="img" aria-label="Doctor in a suit in the clinic" style="background:linear-gradient(90deg,#2a2e38,#6d7380 50%,#c7c9cc)"></div>
  <div class="abs post-date">25<br>SEP</div>
  <h3 class="abs">LOREM IPSUM DOLOR SIT</h3>
  <div class="abs by">BY: ADMIN</div>
  <p class="abs">Lorem ipsum dolor sit amet, con sec tetur adipiscing elit. Duis commodo augue nec elit pellentesque molestie. <em>+ Read More..</em></p>
</article>
<article class="abs post" style="left:778px">
  <div class="post-img" role="img" aria-label="Laser device treating a hand" style="background:linear-gradient(135deg,#5a1a1a,#b04040 50%,#d98f7c)"></div>
  <div class="abs post-date">11<br>JUN</div>
  <h3 class="abs">LOREM IPSUM DOLOR SIT</h3>
  <div class="abs by">BY: ADMIN</div>
  <p class="abs">Lorem ipsum dolor sit amet, con sec tetur adipiscing elit. Duis commodo augue nec elit pellentesque molestie. <em>+ Read More..</em></p>
</article>

<footer class="abs site-footer">
  <h4 style="left:97px">CONTACT US</h4>
  <div class="abs foot-about">Lorem ipsum dolor sit amet, consectetur adipiscing elit. Vestibulum vulputate nunc non porttitor venenatis.</div>
  <div class="foot-line" style="top:175px">
    <svg width="10" height="14" viewBox="0 0 10 14"><path d="M5 0 C2 0 0 2 0 5 C0 8 5 14 5 14 C5 14 10 8 10 5 C10 2 8 0 5 0Z" fill="#2e8be0"/><circle cx="5" cy="5" r="2" fill="#232323"/></svg>
    <span>1820 Canyon Ridge Rd., Ridgeview, Texas<br>70142 (555) 014-2290</span>
  </div>
  <div class="foot-line" style="top:232px">
    <svg width="12" height="12" viewBox="0 0 12 12"><path d="M2 0 L4.5 0 L5.5 3 L4 4.5 C5 6.5 5.5 7 7.5 8 L9 6.5 L12 7.5 L12 10 C12 11 11 12 10 12 C4.5 12 0 7.5 0 2 C0 1 1 0 2 0Z" fill="#2e8be0"/></svg>
    <span>Phone: (555) 014-2291</span>
  </div>
  <div class="foot-line" style="top:255px">
    <svg width="13" height="10" viewBox="0 0 13 10"><rect width="13" height="10" fill="#2e8be0"/><path d="M0 0 L6.5 5.5 L13 0" stroke="#232323" fill="none"/></svg>
    <span>Email: hello@ridgeviewspine.example</span>
  </div>

  <h4 style="left:441px">RELATED LINKS</h4>
  <div class="links" style="left:441px"><div>Accessibility</div><div>Insurance</div><div>Volunteer</div><div>Make a donation</div><div>Our Campaigns</div><div>End loneliness</div></div>
  <div class="links" style="left:598px"><div>Linking policy</div><div>Mobility scooters</div><div>Raise money</div><div>Work for us</div><div>Care in Crisis</div><div>Help Attendance</div></div>

  <h4 style="left:784px">OPENING HOURS</h4>
  <div class="abs hours">
    <div><span>Sat - Tues :</span><span>6.00 AM - 10.00 PM</span></div>
    <div><span>Wed - Thurs :</span><span>8.00 AM - 6.00 PM</span></div>
    <div><span>Friday :</span><span>6.00 AM - 10.00 PM</span></div>
    <div style="border-bottom:none"><span>Sunday :</span><span>Closed</span></div>
  </div>

  <div class="abs foot-bottom">Copyright 2018 <a>ridgeviewspine</a> | All Rights Reserved</div>
  <div class="abs social" style="left:861px"></div>
  <div class="abs social" style="left:910px"></div>
  <div class="abs social" style="left:958px"></div>
  <div class="abs social" style="left:1007px"></div>
  <div class="abs social" style="left:1056px"></div>
</footer>

</body>
</html>
```